High profile consultancy

We need a web design for a company called BK Services. BK as abbreviation for Bold Keystone.

Company focusses on Sourcing (BK Sourcing, focus on ICT), Metrics (BK Metrics; focus on business case analysis and trends in ICT) and Software (BK software; to be developed later on; mainly tools supporting BK soucing and metrics)

Customers base consists of large enterprises, >1000 employees.

Site needs to have menu's for
- services
- login
- about
and a special area ' inspire ' to be able to communicate topics that should inspire our customers to contact us.

but key; it schould communicate our expertise and focus on deep knowlegde of ICT sourcing

Reason: please advice on content management systems to be used to maintain site also please advice on Trovix search clickbids. Will provide feedback on designs shortly.

Target Market(s)

CIO's; board of directors;
company excels in ICT / business knowledge and ability to execute; creates / optimizes relations between ICT suppliers and enterprises.

Requirements
Must have
• website should be easily be found; adaptive by design; accessible by all browsers.
• Need to have a login section for later use
Nice to have
• usage of (draft) logo. see upload.

```html
<!DOCTYPE html>
<html lang="en">
<head>
<meta charset="utf-8">
<title>BK Services</title>
<link rel="stylesheet" href="https://fonts.googleapis.com/css2?family=Arimo:wght@400;700&family=Cinzel:wght@400&family=Roboto+Condensed:wght@300;400;700&display=swap">
<style>
:root{
  --blue:#0b5cb3;
  --blue-deep:#0a2f8c;
  --blue-mid:#1340a8;
  --ink:#222;
  --grey:#555;
  --text:#333;
  --white:#fff;
  --footer-bar:#1b1b1d;
  --link:#1b5fb0;
}
*{margin:0;padding:0;box-sizing:border-box}
html,body{width:788px;height:1200px;overflow:hidden;background:var(--white)}
body{position:relative;font-family:Arimo,Arial,sans-serif;color:var(--text)}
.abs{position:absolute}
/* header */
.site-header{position:absolute;left:0;top:0;width:788px;height:61px;background:var(--white);border-top:2px solid var(--blue)}
.account-tab{position:absolute;left:578px;top:0;width:104px;height:15px;background:var(--blue);color:var(--white);font:700 7px/15px "Cinzel",serif;letter-spacing:.6px;text-align:center;clip-path:polygon(0 0,100% 0,96% 100%,4% 100%)}
.brand{position:absolute;left:107px;top:16px;display:flex;align-items:center;gap:7px}
.brand-dot{width:22px;height:22px;border-radius:50%;background:var(--blue)}
.brand-name{font:400 17px "Roboto Condensed",sans-serif;color:#2c3c5a}
.main-nav{position:absolute;top:31px;left:0;font:400 7.5px "Cinzel",serif;letter-spacing:.8px;color:#444}
.main-nav span{position:absolute;white-space:nowrap}
.header-rule{position:absolute;left:0;top:59px;width:788px;height:3px;background:var(--blue)}
/* hero */
.hero{position:absolute;left:0;top:62px;width:788px;height:400px;
  background:
    radial-gradient(ellipse 150px 120px at 235px 200px,rgba(255,236,200,.85) 0%,rgba(240,215,180,.35) 45%,rgba(0,0,0,0) 100%),
    linear-gradient(180deg,rgba(0,0,0,0) 0%,rgba(0,0,0,0) 50%,rgba(40,38,60,.35) 62%,rgba(90,95,140,.35) 100%),
    linear-gradient(90deg,#6f7e98 0%,#a9b4c2 18%,#b8b6b4 30%,#7d7f8e 48%,#3c3d4c 66%,#16161e 82%,#08080c 100%)}
.hero-title{position:absolute;left:386px;top:184px;color:var(--white);font:400 25px/33px "Cinzel",serif;letter-spacing:.5px}
.hero-copy{position:absolute;left:386px;top:260px;width:296px;color:#e8e8ee;font:400 9.4px/14px Arimo,sans-serif}
.hero-button{position:absolute;left:386px;top:309px;width:99px;height:26px;border:1px solid var(--white);color:var(--white);font:400 9px/24px Arimo,sans-serif;text-align:center}
.hero-rule{position:absolute;left:0;top:460px;width:788px;height:3px;background:var(--blue)}
/* content */
.photo{position:absolute}
.section-title{position:absolute;font:400 12px "Roboto Condensed",sans-serif;color:var(--grey);letter-spacing:.6px;text-transform:uppercase}
.body-copy{position:absolute;font:400 6.4px/9.6px Arimo,sans-serif;color:var(--ink)}
.read-more{position:absolute;font:700 6.4px Arimo,sans-serif;color:var(--link);letter-spacing:.4px}
/* footer */
.site-footer{position:absolute;left:0;top:864px;width:788px;height:296px;background:radial-gradient(ellipse at 50% 20%,var(--blue-mid) 0%,var(--blue-deep) 55%,#061b63 100%)}
.footer-title{position:absolute;font:400 11px "Roboto Condensed",sans-serif;color:#9fb3e6;letter-spacing:.5px;text-transform:uppercase}
.footer-copy{position:absolute;font:400 6.1px/10.2px Arimo,sans-serif;color:#a9b7e0}
.footer-brand{position:absolute;left:110px;top:926px;display:flex;align-items:center;gap:6px}
.footer-brand .brand-dot{width:18px;height:18px;background:#0a2a7e}
.footer-brand .brand-name{font-size:15px;color:#0a2a7e}
.contact-line{position:absolute;left:388px;display:flex;align-items:center;gap:11px;font:700 6.1px Arimo,sans-serif;color:#dfe6fb}
.newsletter{position:absolute;left:535px;top:892px;width:148px;height:99px;background:#1c1e2a}
.newsletter h4{position:absolute;left:28px;top:9px;font:400 6.4px Arimo,sans-serif;color:var(--white);letter-spacing:.2px}
.newsletter p{position:absolute;left:9px;top:25px;font:400 6.2px Arimo,sans-serif;color:#c7c9d3}
.newsletter .field{position:absolute;left:9px;top:41px;width:130px;height:19px;background:#e4e4e8;font:400 6px/19px Arimo,sans-serif;color:#666;padding-left:7px}
.newsletter .submit{position:absolute;left:9px;top:67px;width:130px;height:20px;background:#0b2f9e;font:700 8.5px/20px Arimo,sans-serif;color:var(--white);text-align:center;letter-spacing:.4px}
.footer-rule{position:absolute;left:105px;top:1013px;width:578px;height:1px;background:#2c53b8}
.link-list{position:absolute;list-style:none;font:400 6px Arimo,sans-serif;color:#e4e9fb}
.link-list li{height:12px;line-height:12px}
.link-list li::before{content:"›";color:#9fb3e6;margin-right:5px}
.social{position:absolute;left:535px;font:400 6px Arimo,sans-serif;color:#e4e9fb;display:flex;align-items:center;gap:8px}
.social i{width:11px;height:11px;border-radius:50%;background:var(--white);display:block}
.bottom-bar{position:absolute;left:0;top:1158px;width:788px;height:42px;background:var(--footer-bar);font:400 6.4px Arimo,sans-serif;color:#ddd}
.bottom-bar span{position:absolute;top:18px}
</style>
</head>
<body>

<header class="site-header">
  <div class="account-tab">LOGIN &nbsp;|&nbsp; REGISTER</div>
  <div class="brand"><div class="brand-dot"></div><div class="brand-name">BK Services</div></div>
  <nav class="main-nav">
    <span style="left:391px">HOME</span>
    <span style="left:448px">SERVICES</span>
    <span style="left:520px">ABOUT</span>
    <span style="left:581px">INSPIRE</span>
    <span style="left:646px">CONTACT</span>
  </nav>
</header>
<div class="header-rule"></div>

<section class="hero" role="img" aria-label="Business people in silhouette standing by tall sunlit office windows above a city, reflected on a glossy floor"></section>
<h1 class="hero-title">Ensuring the Quality<br>of Your Service</h1>
<p class="hero-copy">Lorem ipsum dolor sit amet, consectetur adipisicing elit, sed do eiusmod tempor incididunt ut labore et dolore magna aliqua.</p>
<div class="hero-button">Learn More</div>
<div class="hero-rule"></div>

<div class="photo" role="img" aria-label="Team of consultants gathered around a laptop in a bright office" style="left:105px;top:499px;width:280px;height:120px;background:radial-gradient(ellipse 60px 40px at 265px 95px,rgba(214,222,60,.7),rgba(214,222,60,0) 100%),linear-gradient(90deg,#e9edf2 0%,#b8bcc4 20%,#7d8592 38%,#c9b9a6 52%,#8e97a8 70%,#eef1f4 88%,#f7f8fa 100%)"></div>
<h2 class="section-title" style="left:401px;top:518px">About BK Services</h2>
<p class="body-copy" style="left:400px;top:540px;width:283px">Lorem ipsum dolor sit amet, consectetur adipisicing elit, sed do eiusmod tempor incididunt ut labore et dolore magna aliqua. Ut enim ad minim veniam, quis nostrud exercitation. Lorem ipsum dolor sit amet, consectetur adipisicing elit, sed do eiusmod tempor incididunt ut labore et dolore magna aliqua. Ut enim ad minim veniam, quis nostrud exercitation.</p>
<div class="read-more" style="left:400px;top:592px">READ MORE &nbsp;›</div>

<h2 class="section-title" style="left:105px;top:653px">BK Sourcing</h2>
<h2 class="section-title" style="left:302px;top:653px">BK Metrics</h2>
<h2 class="section-title" style="left:499px;top:653px">BK Software</h2>

<div class="photo" role="img" aria-label="Business meeting around a conference table with laptops" style="left:105px;top:676px;width:183px;height:86px;background:linear-gradient(180deg,rgba(255,255,255,0) 55%,rgba(230,232,236,.8) 100%),linear-gradient(90deg,#3a3d45 0%,#d9dde2 25%,#6b717b 45%,#c5c9cf 62%,#30333a 85%,#e3e6ea 100%)"></div>
<div class="photo" role="img" aria-label="Hands reviewing printed blue bar charts on a desk" style="left:302px;top:676px;width:183px;height:86px;background:radial-gradient(ellipse 70px 25px at 110px 68px,rgba(90,150,210,.6),rgba(90,150,210,0) 100%),linear-gradient(120deg,#7f8794 0%,#e8eaee 30%,#f6f7f9 55%,#d9dde2 75%,#6a3b30 92%,#2d2b2e 100%)"></div>
<div class="photo" role="img" aria-label="Hand using a tablet showing blue charts" style="left:499px;top:676px;width:183px;height:86px;background:radial-gradient(ellipse 55px 35px at 125px 38px,rgba(120,175,225,.8),rgba(120,175,225,0) 100%),linear-gradient(110deg,#f3f3f1 0%,#e2d6c8 28%,#f4f5f7 50%,#cddceb 70%,#eef1f4 100%)"></div>

<p class="body-copy" style="left:105px;top:774px;width:185px">Lorem ipsum dolor sit amet, consectetur adipisicing elit, sed do eiusmod tempor incididunt ut labore et dolore magna aliqua. Ut enim ad minim veniam, quis nostrud exercitation.</p>
<p class="body-copy" style="left:302px;top:774px;width:185px">Lorem ipsum dolor sit amet, consectetur adipisicing elit, sed do eiusmod tempor incididunt ut labore et dolore magna aliqua. Ut enim ad minim veniam, quis nostrud exercitation.</p>
<p class="body-copy" style="left:499px;top:774px;width:185px">Lorem ipsum dolor sit amet, consectetur adipisicing elit, sed do eiusmod tempor incididunt ut labore et dolore magna aliqua. Ut enim ad minim veniam, quis nostrud exercitation.</p>
<div class="read-more" style="left:105px;top:816px">READ MORE &nbsp;›</div>
<div class="read-more" style="left:302px;top:816px">READ MORE &nbsp;›</div>
<div class="read-more" style="left:499px;top:816px">READ MORE &nbsp;›</div>

<footer class="site-footer"></footer>
<div class="footer-brand"><div class="brand-dot"></div><div class="brand-name">BK Services</div></div>

<h3 class="footer-title" style="left:238px;top:893px">What We Do</h3>
<p class="footer-copy" style="left:238px;top:910px;width:120px">Duis mollis, est non commodo luctus, nisi erat porttitor ligula, eget lacinia odio sem nec elit. Vestibulum id ligula porta felis euismod semper. Integer posuere erat a ante.</p>
<p class="footer-copy" style="left:238px;top:968px;width:120px">Vestibulum id ligula porta felis euismod semper. Integer posuere erat a ante.</p>

<h3 class="footer-title" style="left:384px;top:893px">Contact</h3>
<p class="footer-copy" style="left:388px;top:910px;width:115px">There are many variations of passages of Lorem Ipsum available, but the majority have suffered alteration.</p>
<div class="contact-line" style="top:954px">
  <svg width="7" height="9" viewBox="0 0 7 9"><path d="M3.5 0a3.5 3.5 0 0 0-3.5 3.5C0 6 3.5 9 3.5 9S7 6 7 3.5A3.5 3.5 0 0 0 3.5 0z" fill="#8fa3d6"/><circle cx="3.5" cy="3.5" r="1.2" fill="#1340a8"/></svg>Northgate</div>
<div class="contact-line" style="top:970px">
  <svg width="9" height="7" viewBox="0 0 9 7"><rect width="9" height="7" fill="#8fa3d6"/><path d="M0 0l4.5 3.5L9 0" stroke="#1340a8" fill="none"/></svg>info@bkservices-mail.com</div>
<div class="contact-line" style="top:985px">
  <svg width="8" height="8" viewBox="0 0 8 8"><path d="M1 0h2l1 2-1.2 1a5 5 0 0 0 2.2 2.2L6 4l2 1v2a1 1 0 0 1-1 1A7 7 0 0 1 0 1a1 1 0 0 1 1-1z" fill="#8fa3d6"/></svg>890-01234-56789</div>

<div class="newsletter">
  <svg class="abs" style="left:9px;top:8px" width="12" height="9" viewBox="0 0 12 9"><rect width="12" height="9" fill="#8e93a3"/><path d="M0 0l6 4.5L12 0" stroke="#1c1e2a" fill="none"/></svg>
  <h4>SUBSCRIBE TO OUR NEWSLETTER</h4>
  <p>Sign up and get the latest news and updates.</p>
  <div class="field">Enter your email address</div>
  <div class="submit">SUBSCRIBE TODAY</div>
</div>

<div class="footer-rule"></div>

<h3 class="footer-title" style="left:104px;top:1040px">Site Links</h3>
<h3 class="footer-title" style="left:253px;top:1040px">Services</h3>
<h3 class="footer-title" style="left:535px;top:1040px">Social</h3>
<ul class="link-list" style="left:105px;top:1058px"><li>Home</li><li>About</li><li>Links</li><li>Blog</li><li>Contact</li></ul>
<ul class="link-list" style="left:254px;top:1058px"><li>BK Service</li><li>BK Service</li><li>BK Service</li><li>BK Service</li><li>BK Service</li></ul>
<ul class="link-list" style="left:387px;top:1058px"><li>BK Service</li><li>BK Service</li><li>BK Service</li><li>BK Service</li><li>BK Service</li></ul>
<div class="social" style="top:1062px"><i></i>Like us on Friendnet</div>
<div class="social" style="top:1081px"><i></i>Follow us on Chirper</div>
<div class="social" style="top:1100px"><i></i>Add us in Linkpro</div>

<div class="bottom-bar">
  <span style="left:105px">Copyright 2013 © BK Services - All Rights Reserved</span>
  <span style="left:534px">Site Map &nbsp;&nbsp;•&nbsp;&nbsp; Privacy Policy &nbsp;&nbsp;•&nbsp;&nbsp; Disclaimer</span>
</div>

</body>
</html>
```